Business Card Design

Please visit www.MarkDorsey.com to acquire information for business card.

Back Side of Card:
a lifetime of experience working for you.

With over 25 years in the construction industry, well over a decade as a licensed Subcontractor / General Contractor and nearly 10 years as a licensed Realtor, I have excelled and cultivated a working knowledge of how all the pieces fit together.

Here is a link to folder.
https://files.examplecloud.net/folderview?id=7Qk2mXrTpLw9zVbN4sHcDyUeFaGj&usp=sharing

Industry/Entity Type

Construction

Contact Information for Business Card

Company: Mark Dorsey, LLC.
Address: 31872 W. Cedar Hollow Blvd. Suite 207-418
Name: Mark Dorsey
Phone: (623) 587-2914
Web: www.MarkDorsey.com
Type of services offered: Architectural Design, 3D Models, Renderings & Animation - Construction Documents - Project Managment.

```html
<!DOCTYPE html>
<html lang="en">
<head>
<meta charset="utf-8">
<title>Mark Dorsey, LLC. — Business Card</title>
<link rel="stylesheet" href="https://fonts.googleapis.com/css2?family=Inconsolata:wght@400;700&family=Oswald:wght@500&family=Ubuntu+Mono:ital,wght@0,400;0,700;1,400;1,700&display=swap">
<style>
  :root {
    --card-blue: #1d169c;
    --ink: #111111;
    --paper: #ffffff;
    --mark-blue: #6a64c6;
    --mark-edge: #16127a;
    --band: #0d0d16;
    --photo-dark: #15120e;
    --photo-warm: #6b4a2a;
    --thumb-light: #d9dcdf;
    --thumb-green: #5d6b47;
  }
  * { margin: 0; padding: 0; box-sizing: border-box; }
  html, body { width: 1200px; height: 480px; overflow: hidden; background: var(--paper); }
  .sheet { position: relative; width: 1200px; height: 480px; }
  .side-label {
    position: absolute; top: 50px;
    font: 700 24px/1 "Inconsolata", monospace; color: var(--ink);
  }
  .side-label--front { left: 32px; }
  .side-label--back { left: 612px; }

  .card { position: absolute; background: var(--card-blue); color: var(--paper); }
  .card--front { left: 24px; top: 97px; width: 548px; height: 323px; overflow: hidden; }
  .card--back { left: 594px; top: 97px; width: 549px; height: 206px; }

  .front-mark {
    position: absolute; left: 103px; top: 8px; width: 66px; height: 66px;
    background: var(--paper); border: 2px solid var(--ink);
    display: flex; align-items: center; justify-content: center; text-align: center;
    font: 700 11px/1.15 "Ubuntu Mono", monospace; color: var(--card-blue); padding: 4px;
  }
  .company-name {
    position: absolute; left: 178px; top: 16px;
    font: italic 700 27px/1 "Ubuntu Mono", monospace; letter-spacing: 0.5px;
  }
  .company-address {
    position: absolute; left: 174px; top: 53px;
    font: italic 400 15.5px/1 "Ubuntu Mono", monospace;
  }
  .rules { position: absolute; left: 0; top: 0; }

  .thumb { position: absolute; }
  .thumb--roof { left: 12px; top: 90px; width: 72px; height: 60px;
    background: linear-gradient(135deg, #f2f3f3, var(--thumb-light)); }
  .thumb--plan { left: 24px; top: 150px; width: 88px; height: 62px;
    background: linear-gradient(160deg, #f7f7f7, #cfd3d6); }
  .thumb--site { left: 36px; top: 212px; width: 86px; height: 62px;
    background: linear-gradient(150deg, #8a8f6e, var(--thumb-green) 60%, #3e4232); }
  .thumb--frame { left: 110px; top: 250px; width: 110px; height: 70px;
    background: linear-gradient(160deg, #b7b9ae, #6f766c 55%, #4b5248); }

  .photo-night {
    position: absolute; left: 306px; top: 98px; width: 232px; height: 158px;
    background: radial-gradient(ellipse at 30% 70%, var(--photo-warm), var(--photo-dark) 70%);
    -webkit-mask-image: linear-gradient(90deg, transparent 0, #000 22%, #000 80%, transparent 100%);
            mask-image: linear-gradient(90deg, transparent 0, #000 22%, #000 80%, transparent 100%);
  }

  .services { position: absolute; left: 137px; top: 106px;
    font: 500 12.5px/1 "Oswald", sans-serif; list-style: none; }
  .services__title { margin-bottom: 8px; }
  .services__item { margin-bottom: 9px; }
  .services__item::before { content: "\2731\00a0"; font-size: 9px; vertical-align: 2px; }
  .services__item:nth-child(2) { padding-left: 8px; }
  .services__item:nth-child(3) { padding-left: 20px; }
  .services__item:nth-child(4) { padding-left: 32px; }
  .services__item:nth-child(5) { padding-left: 44px; }

  .person-name {
    position: absolute; left: 272px; top: 241px;
    font: italic 700 22px/1 "Ubuntu Mono", monospace;
    color: var(--card-blue); -webkit-text-stroke: 1px var(--paper);
  }
  .contact { position: absolute; left: 320px; top: 275px;
    font: italic 400 16px/22px "Ubuntu Mono", monospace; }

  .back-mark {
    position: absolute; left: 209px; top: 23px; width: 130px; height: 130px;
    background: var(--mark-blue); border: 2px solid var(--mark-edge);
    outline: 1px solid var(--mark-blue); outline-offset: 2px;
    display: flex; align-items: center; justify-content: center; text-align: center;
    font: 700 18px/1.2 "Ubuntu Mono", monospace; color: var(--mark-edge); padding: 10px;
  }
  .tagline { position: absolute; left: 10px; top: 164px;
    font: 400 21px/1 "Ubuntu Mono", monospace; letter-spacing: 0.2px; }
  .back-band { position: absolute; left: 0; bottom: 0; width: 100%; height: 11px; background: var(--band); }

  .bio {
    position: absolute; left: 594px; top: 309px; width: 549px;
    text-align: center; color: var(--ink);
    font: 700 14.5px/17px "Inconsolata", monospace;
  }
</style>
</head>
<body>
<main class="sheet">
  <h2 class="side-label side-label--front">Front Business Card</h2>
  <h2 class="side-label side-label--back">Back</h2>

  <section class="card card--front" aria-label="Front of card">
    <div class="thumb thumb--roof" role="img" aria-label="Roof framing 3D model"></div>
    <div class="thumb thumb--plan" role="img" aria-label="Site plan drawing"></div>
    <div class="thumb thumb--site" role="img" aria-label="Aerial rendering of a building site"></div>
    <div class="thumb thumb--frame" role="img" aria-label="Steel frame model of a building"></div>
    <div class="photo-night" role="img" aria-label="Night rendering of a lit patio with pergola and fire feature"></div>

    <svg class="rules" width="548" height="323" viewBox="0 0 548 323" aria-hidden="true">
      <line x1="24" y1="81" x2="294" y2="81" stroke="#fff" stroke-width="3"/>
      <line x1="256" y1="88" x2="526" y2="88" stroke="#0d0d16" stroke-width="3"/>
      <polyline points="84,92 84,146 114,146 114,198 138,198 138,245 225,245" fill="none" stroke="#fff" stroke-width="3"/>
      <polyline points="97,120 97,140 127,140 127,192 150,192 150,232 240,232" fill="none" stroke="#fff" stroke-width="3"/>
    </svg>

    <div class="front-mark">Mark Dorsey, LLC.</div>
    <h1 class="company-name">Mark Dorsey, LLC.</h1>
    <p class="company-address">31872 W. Cedar Hollow Blvd. Suite 207-418</p>

    <ul class="services">
      <li class="services__title">Type of services offered:</li>
      <li class="services__item">Architectural Design, 3D Models</li>
      <li class="services__item">Renderings &amp; Animation</li>
      <li class="services__item">Construction Documents</li>
      <li class="services__item">Project Management</li>
    </ul>

    <p class="person-name">Mark Dorsey</p>
    <p class="contact">Phone: (623) 587-2914<br>Web: www.MarkDorsey.com</p>
  </section>

  <section class="card card--back" aria-label="Back of card">
    <div class="back-mark">Mark Dorsey, LLC.</div>
    <p class="tagline">A lifetime of experience working for you.</p>
    <div class="back-band"></div>
  </section>

  <p class="bio">With over 25 years in the construction industry,<br>
    well over a decade as a licensed Subcontractor /<br>
    General Contractor and nearly 10 years as a<br>
    licensed Realtor,<br>
    I have excelled and cultivated a working knowledge<br>
    of how all the pieces fit together.</p>
</main>
</body>
</html>
```